Einladungskarten-Design zur Einweihung von neuen Räumlichkeiten eines Planungsdienstleisters für Elektro- sowie IT-Lösungen
Zielgruppe
Planungsleistung für Elektro sowie IT Lösungen
Aufgabenstellung
Einladung zur Einweihung der neuen Räumlichkeiten, am 09. November 2024, beginn 16:00 Uhr. Einladung durch Geschäftsführer E-Strommark GmbH - Tobias Kernbichl und Geschäftsführer IT-Strommark GmbH - Florian Wetzbacher
Ort:
E-Strommark GmbH, IT-Strommark GmbH
Lerchenfeldstr. 14
88472 Ebersweiler
Anmeldung, Rückmeldung per Mail an
info@e-strommark.de

```html
<!DOCTYPE html>
<html lang="de">
<head>
<meta charset="utf-8">
<title>Einladung zur Einweihung – E-Strommark &amp; IT-Strommark</title>
<link rel="stylesheet" href="https://fonts.googleapis.com/css2?family=Antonio:wght@400;500&family=Arimo:wght@400;700&display=swap">
<style>
  :root {
    --ink: #0b0b0b;
    --grey-text: #6f6f73;
    --label: #5f5f63;
    --accent-green: #9cc727;
    --house-blue: #a9dbf5;
    --veil: rgba(214, 208, 230, 0.82);
    --paper: #ffffff;
  }
  * { margin: 0; padding: 0; box-sizing: border-box; }
  html, body { width: 1200px; height: 408px; overflow: hidden; background: var(--paper); }
  body { position: relative; font-family: "Arimo", Arial, sans-serif; }

  .card { position: absolute; top: 0; height: 408px; overflow: hidden; }

  /* Front */
  .card--front { left: 0; width: 578px; }
  .front-photo {
    position: absolute; inset: 0;
    background:
      radial-gradient(ellipse at 62% 55%, rgba(235,250,250,0.9) 0%, rgba(120,210,205,0.6) 30%, rgba(0,0,0,0) 60%),
      linear-gradient(90deg, #1d2a6a 0%, #1f5f86 35%, #29a6a0 70%, #1a7f8a 100%);
  }
  .front-veil {
    position: absolute; left: 30px; top: 29px; width: 519px; height: 350px;
    background: var(--veil);
  }
  .front-title {
    position: absolute; left: 30px; top: 78px; width: 519px;
    font-family: "Antonio", "Arial Narrow", sans-serif; font-weight: 500;
    color: var(--ink); text-align: center; text-transform: uppercase;
    font-size: 66px; line-height: 70px; letter-spacing: -2px;
    transform: scaleX(0.9); transform-origin: center;
  }
  .front-subtitle {
    position: absolute; left: 30px; top: 230px; width: 519px;
    font-family: "Antonio", "Arial Narrow", sans-serif; font-weight: 400;
    color: var(--ink); text-align: center;
    font-size: 28px; line-height: 30px; letter-spacing: -0.5px;
  }

  /* Back */
  .card--back { left: 622px; width: 578px; border: 1px solid #d6d6d6; }
  .back-photo {
    position: absolute; left: 0; top: 0; width: 399px; height: 100%;
    background: linear-gradient(100deg, #e6e6f0 0%, #e9f3f4 45%, #e4f4f2 70%, #ecf1f6 100%);
  }
  .back-side { position: absolute; left: 399px; top: 0; width: 179px; height: 100%; background: var(--paper); }

  .back-heading {
    position: absolute; left: 22px;
    font-family: "Antonio", "Arial Narrow", sans-serif; font-weight: 400;
    color: var(--accent-green); font-size: 34px; line-height: 1;
  }
  .back-heading--top { top: 22px; }
  .back-heading--closing { top: 313px; font-size: 35px; }

  .info { position: absolute; left: 22px; font-size: 13.5px; color: var(--grey-text); white-space: nowrap; }
  .info--label { font-weight: 700; color: var(--label); }

  .signatures { position: absolute; left: 22px; top: 358px; font-size: 13.5px; line-height: 20px; color: var(--grey-text); white-space: nowrap; }

  .brand { position: absolute; left: 420px; width: 150px; }
  .brand-name { font-family: "Arimo", Arial, sans-serif; font-weight: 400; font-size: 17px; color: var(--label); }
  .brand--electro { top: 26px; }
  .brand--it { top: 370px; }

  .house-art { position: absolute; left: 406px; top: 115px; width: 164px; height: 180px;
    background: linear-gradient(180deg, var(--house-blue), #c4e7f9); border-radius: 4px; }
</style>
</head>
<body>
  <section class="card card--front">
    <div class="front-photo" role="img" aria-label="Abstraktes Foto: leuchtende Datenlichtstrahlen in Türkis und Blau"></div>
    <div class="front-veil"></div>
    <h1 class="front-title">Herzliche<br>Einladung</h1>
    <p class="front-subtitle">zur Einweihung unserer<br>Räumlichkeiten</p>
  </section>

  <section class="card card--back">
    <div class="back-photo" role="img" aria-label="Blasses Hintergrundfoto mit Lichtstrahlen"></div>
    <div class="back-side"></div>

    <h2 class="back-heading back-heading--top">Einladung</h2>
    <p class="info info--label" style="top:69px">Zeit:</p>
    <p class="info" style="top:95px">09. November 2024, beginn 16:00 Uhr</p>
    <p class="info info--label" style="top:134px">Ort:</p>
    <p class="info" style="top:160px">E-Strommark GmbH, IT-Strommark GmbH</p>
    <p class="info" style="top:185px">Lerchenfeldstr. 14</p>
    <p class="info" style="top:211px">88472 Ebersweiler</p>
    <p class="info info--label" style="top:247px">Anmeldung, Rückmeldung per Mail an</p>
    <p class="info" style="top:273px">info@e-strommark.de</p>

    <h2 class="back-heading back-heading--closing">Wir freuen uns auf Sie!</h2>
    <p class="signatures">Geschäftsführer E-Strommark GmbH - Tobias Kernbichl und<br>Geschäftsführer IT-Strommark GmbH - Florian Wetzbacher</p>

    <div class="brand brand--electro">
      <div class="brand-name">E-STROMMARK</div>
    </div>
    <div class="house-art" role="img" aria-label="Illustration: hellblaues Haus mit Schlüssel"></div>
    <div class="brand brand--it">
      <div class="brand-name">IT-STROMMARK</div>
    </div>
  </section>
</body>
</html>
```